K & R Acreage Works. Business card design

We need a business card designed for a new business. We have a bulldozer and tractor service. We clear land and make wildlife food plots. We provide disking, bush hogging, and site prep services.
I have attached an image of a business card that I like and would like my business cards to look similar.

Target Market(s)

anyone needing bulldozer and/or tractor services

Industry/Entity Type

Business

Contact Information for Business Card

K & R Acreage Works, Operated by 7-M-Ranch
Doug Pelham
601-473-5826
dpr4178@mailvexo.com

Font styles to use
Sans Serif

Colors

Designer to choose colors to be used in the design.

Requirements
Must have
• image of tractor and bulldozer
• Land Clearing
• Wildlife food plots
• Bush Hogging
• Disking
• Site prep
Nice to have
• i have included a image of a business card that i like. I would like mine to be similar.

```html
<!DOCTYPE html>
<html lang="en">
<head>
<meta charset="UTF-8">
<title>K &amp; R Acreage Works – Business Card</title>
<link href="https://fonts.googleapis.com/css2?family=Montserrat:wght@400;500;600&family=Oswald:wght@500&display=swap" rel="stylesheet">
<style>
  :root {
    --backdrop: #d3ecef;
    --charcoal: #333437;
    --teal: #3f8b92;
    --teal-light: #63cbc8;
    --white: #ffffff;
    --ground-light: #c9b79a;
    --ground-dark: #8c7a5c;
    --grass: #5f7a3a;
    --sky: #6fa3d8;
  }
  * { margin: 0; padding: 0; box-sizing: border-box; }
  html, body { width: 1200px; height: 800px; overflow: hidden; }
  body { background: var(--backdrop); position: relative; font-family: "Montserrat", sans-serif; }

  .card {
    position: absolute; left: 100px; top: 114px;
    width: 1000px; height: 572px; overflow: hidden;
    background: var(--charcoal);
  }
  .photo { position: absolute; }
  .photo-ground {
    left: 0; top: 0; width: 600px; height: 340px;
    background: linear-gradient(160deg, #7f8d5a 0%, var(--ground-light) 45%, var(--ground-dark) 100%);
  }
  .photo-tractor {
    left: 560px; top: 0; width: 440px; height: 340px;
    background: radial-gradient(ellipse at 55% 55%, #d9532a 0%, #c85a30 22%, var(--grass) 50%, #3f5a2a 100%);
  }
  .photo-dozer {
    left: 0; top: 120px; width: 290px; height: 220px;
    background: linear-gradient(180deg, var(--sky) 0%, #b9cde0 40%, #c9a93a 62%, #8d7a5a 100%);
  }
  .shapes { position: absolute; inset: 0; width: 1000px; height: 572px; }

  .brand { position: absolute; left: 330px; top: 88px; display: flex; align-items: center; gap: 14px; }
  .brand-dot { width: 34px; height: 34px; border-radius: 50%; background: var(--teal-light); flex: none; }
  .brand-name {
    font-family: "Oswald", sans-serif; font-weight: 500; font-size: 50px;
    line-height: 1; color: var(--white); letter-spacing: 0.5px; white-space: nowrap;
  }
  .brand-sub {
    position: absolute; left: 378px; top: 150px;
    font-size: 22px; letter-spacing: 1.5px; color: var(--white); white-space: nowrap;
  }

  .contact { position: absolute; left: 44px; top: 372px; color: var(--white); }
  .contact-name {
    font-weight: 600; font-size: 42px; letter-spacing: 2px; color: var(--teal-light);
    margin-bottom: 18px; white-space: nowrap;
  }
  .contact-line { display: flex; align-items: center; gap: 14px; font-size: 27px; margin-bottom: 10px; white-space: nowrap; }
  .contact-line svg { width: 32px; height: 28px; flex: none; }

  .services { position: absolute; top: 372px; list-style: none; color: var(--white); font-size: 23px; font-weight: 500; }
  .services li { position: absolute; white-space: nowrap; }
</style>
</head>
<body>
  <div class="card">
    <div class="photo photo-ground" role="img" aria-label="Photo of cleared dirt ground at a work site"></div>
    <div class="photo photo-tractor" role="img" aria-label="Photo of an orange tractor with front loader bucket in tall grass"></div>
    <div class="photo photo-dozer" role="img" aria-label="Photo of a yellow bulldozer pushing dirt"></div>

    <svg class="shapes" viewBox="0 0 1000 572" aria-hidden="true">
      <polygon points="310,78 760,40 760,172 290,200" fill="var(--charcoal)"/>
      <polygon points="0,340 570,340 690,572 0,572" fill="var(--charcoal)"/>
      <polygon points="570,340 606,340 726,572 690,572" fill="var(--teal-light)"/>
      <polygon points="606,310 1000,290 1000,572 726,572" fill="var(--teal)"/>
      <polygon points="570,340 606,310 606,340" fill="var(--teal-light)"/>
    </svg>

    <div class="brand">
      <span class="brand-dot"></span>
      <span class="brand-name">K &amp; R ACREAGE WORKS</span>
    </div>
    <div class="brand-sub">OPERATED BY 7-M-RANCH</div>

    <div class="contact">
      <div class="contact-name">DOUG PELHAM</div>
      <div class="contact-line">
        <svg viewBox="0 0 32 28"><path d="M3 10 Q16 0 29 10 L29 13 L23 13 L22 9 Q16 6 10 9 L9 13 L3 13 Z" fill="var(--teal-light)"/><rect x="7" y="14" width="18" height="12" rx="2" fill="var(--teal-light)"/><circle cx="16" cy="20" r="3" fill="var(--charcoal)"/></svg>
        <span>601-473-5826</span>
      </div>
      <div class="contact-line">
        <svg viewBox="0 0 32 28"><rect x="2" y="5" width="28" height="19" fill="var(--teal-light)"/><polyline points="2,5 16,16 30,5" fill="none" stroke="var(--charcoal)" stroke-width="2.5"/></svg>
        <span>dpr4178@mailvexo.com</span>
      </div>
    </div>

    <ul class="services">
      <li style="left:640px; top:0;">Land Clearing</li>
      <li style="left:664px; top:36px;">Wildlife food plots</li>
      <li style="left:690px; top:72px;">Bush Hogging</li>
      <li style="left:716px; top:108px;">Disking</li>
      <li style="left:742px; top:144px;">Site prep</li>
    </ul>
  </div>
</body>
</html>
```